Business card for home decor store and design

I need a business card for my home decor boutique that’s professional looking boho/rustic. We sell vintage furniture, vintage finds, lamps, throws, rugs. We also carry a Diy paint line for refinishing furniture. We offer workshop on painting furniture, private or group setting. We in the heart of Old Town Red Bluff. We love to design, build and restore. Family owned small business. Our style is rustic boho farmhouse. We search for one of a kind found and repurposed items. We love vintage home decor, vintage windows.

Target Market(s)

Home decor

Industry/Entity Type

Home Accessories

Contact Information for Business Card

Have a rustic look/boho

Font styles to use
Serif
Script

Requirements
Must have
• Logo

```html
<!DOCTYPE html>
<html lang="en">
<head>
<meta charset="utf-8">
<title>Willow &amp; Kiln Co. — Business Card</title>
<link href="https://fonts.googleapis.com/css2?family=Oswald:wght@500&family=Roboto:wght@300;400&display=swap" rel="stylesheet">
<style>
  :root {
    --backdrop: #4a4a4c;
    --card: #333335;
    --edge: #ffffff;
    --ink: #f2f2f2;
    --ink-soft: #d6d6d6;
    --rule: #9a9a9a;
    --mark: #a6a6a8;
  }
  html, body {
    margin: 0;
    width: 1200px;
    height: 1124px;
    overflow: hidden;
    background: var(--backdrop);
  }
  .sheet {
    position: relative;
    width: 1200px;
    height: 1124px;
  }
  .card {
    position: absolute;
    left: 220px;
    width: 760px;
    height: 434px;
    background: var(--card);
    box-shadow: 0 10px 28px rgba(0,0,0,0.35);
    color: var(--ink);
    font-family: "Roboto", sans-serif;
    overflow: hidden;
  }
  .card::after {
    content: "";
    position: absolute;
    left: 0; right: 0; bottom: 0;
    height: 12px;
    background: var(--edge);
  }
  .card--front { top: 80px; }
  .card--back  { top: 590px; }

  .brand {
    position: absolute;
    left: 0; right: 0; top: 0; bottom: 12px;
    display: flex;
    align-items: center;
    justify-content: center;
    gap: 18px;
  }
  .brand__ring {
    width: 30px;
    height: 30px;
    border-radius: 50%;
    border: 2px solid var(--mark);
    box-sizing: border-box;
  }
  .brand__name {
    font-family: "Roboto", sans-serif;
    font-weight: 300;
    font-size: 44px;
    letter-spacing: 2px;
    color: var(--mark);
  }

  .person {
    position: absolute;
    right: 420px;
    top: 150px;
    text-align: right;
  }
  .person__name {
    font-family: "Oswald", sans-serif;
    font-weight: 500;
    font-size: 36px;
    letter-spacing: 1.5px;
    line-height: 1.1;
    text-transform: uppercase;
    color: var(--ink);
  }
  .person__role {
    font-weight: 300;
    font-size: 23px;
    color: var(--ink-soft);
    margin-top: 2px;
  }
  .divider {
    position: absolute;
    left: 362px;
    top: 150px;
    width: 1px;
    height: 92px;
    background: var(--rule);
  }
  .contacts {
    position: absolute;
    left: 388px;
    top: 148px;
    margin: 0;
    padding: 0;
    list-style: none;
  }
  .contacts li {
    display: flex;
    align-items: center;
    gap: 14px;
    font-weight: 300;
    font-size: 22px;
    line-height: 32px;
    color: var(--ink);
  }
  .contacts svg {
    width: 18px;
    height: 18px;
    fill: none;
    stroke: var(--ink);
    stroke-width: 1.6;
  }
  .contacts .icon-fill {
    fill: var(--ink);
    stroke: none;
  }
  .address {
    position: absolute;
    left: 0; right: 0;
    bottom: 60px;
    text-align: center;
    font-weight: 300;
    font-size: 21px;
    color: var(--ink-soft);
  }
</style>
</head>
<body>
<main class="sheet">
  <section class="card card--front" aria-label="Card front">
    <div class="brand">
      <span class="brand__ring"></span>
      <span class="brand__name">Willow &amp; Kiln Co.</span>
    </div>
  </section>

  <section class="card card--back" aria-label="Card back">
    <div class="person">
      <div class="person__name">Jonathan Smith</div>
      <div class="person__role">Manager</div>
    </div>
    <div class="divider"></div>
    <ul class="contacts">
      <li>
        <svg viewBox="0 0 20 20" aria-hidden="true"><path class="icon-fill" d="M5 2.5l3 3-1.8 2a10 10 0 0 0 6.3 6.3l2-1.8 3 3-2 2.2C9 17 3 11 2.8 4.5z"/></svg>
        <span>123-456-2100</span>
      </li>
      <li>
        <svg viewBox="0 0 20 20" aria-hidden="true"><rect x="2" y="4.5" width="16" height="11" rx="1"/><path d="M2.5 5l7.5 6 7.5-6"/></svg>
        <span>youremail@mailbox.com</span>
      </li>
      <li>
        <svg viewBox="0 0 20 20" aria-hidden="true"><circle cx="10" cy="10" r="7.5"/><ellipse cx="10" cy="10" rx="3.2" ry="7.5"/><path d="M2.5 10h15M4 6h12M4 14h12"/></svg>
        <span>www.yourwebsite.com</span>
      </li>
    </ul>
    <div class="address">Your address, city, state, ZIP 0000</div>
  </section>
</main>
</body>
</html>
```